Marketing Software requires Fun and Young Business Card Design

We are looking for a new business card design for a start-up marketing campaign management software that is

- fun
- young/fresh
- engaging
- playful
- new kid on the blog
- wants to catch attention

Check out our website: www.zintaropq.com and watch the first video on the homepage. That way you will get a good picture of the product and the target group.

The current business card (attached) is too mainstream and does not catch the attention that we are looking for.
Attached you will find the company logo, some support images from our website and the current business card design.

Company colours: Zintaro Green
RGB 166 / 176 / 12
CMYK needs conversion

Company font:
Titillium for logo copy
Calibri for content copy

Target Market(s)

- marketing people - design, ad and marketing agency people - main market location: Western Europe and North America

Industry/Entity Type

Marketing

Requirements
Must have
• Information that we would like to have on the BC:
Name: Martin Oakes
Function: CEO
Email: martino@zintaropq.com
Mobile: +44 7912 584 207
Website: www.zintaropq.com (maybe)
Nice to have
• In the supporting files you will find some images from the website that could be reused but is not essential.
We liked the idea of the origami look and feel however this might not necessarily the winner.
We also like our robot from our video on the website www.zintaropq.com.
A call to action to try our product for free might be nice (get a free trial@www.zintaropq.com)

We are looking forward to seeing something new than the standard business card.

```html
<!DOCTYPE html>
<html lang="en">
<head>
<meta charset="utf-8">
<title>Zintaro business card – front and back</title>
<link rel="stylesheet" href="https://fonts.googleapis.com/css2?family=Titillium+Web:wght@400;600;700&family=Carlito:wght@400;700&family=Signika:wght@700&display=swap">
<style>
  :root {
    --zintaro-green: #a6b00c;
    --deep-green: #2e7d32;
    --mid-green: #4f9a2c;
    --lime: #c4d62a;
    --pale-lime: #e3ecb0;
    --slate: #55585c;
    --ink: #3a3a3a;
    --paper: #ffffff;
    --stage: #7a5236;
  }
  * { box-sizing: border-box; margin: 0; padding: 0; }
  html, body { width: 1200px; height: 401px; overflow: hidden; }
  body { background: var(--stage); position: relative; font-family: "Carlito", "Calibri", sans-serif; }

  .card {
    position: absolute;
    width: 525px;
    height: 300px;
    overflow: hidden;
    box-shadow: 0 2px 6px rgba(0,0,0,.35);
  }
  .card--front { left: 40px; top: 37px; background: var(--paper); }
  .card--back { left: 626px; top: 33px; }

  .accent-band {
    position: absolute;
    left: 270px;
    top: 0;
    width: 60px;
    height: 100%;
    background: linear-gradient(90deg, var(--slate) 0%, var(--lime) 45%, var(--mid-green) 75%, var(--pale-lime) 100%);
  }

  .brand {
    position: absolute;
    left: 16px;
    top: 128px;
    display: flex;
    align-items: center;
    gap: 8px;
  }
  .brand__dot { width: 14px; height: 14px; border-radius: 50%; background: var(--zintaro-green); }
  .brand__name {
    font-family: "Titillium Web", sans-serif;
    font-weight: 700;
    font-size: 40px;
    line-height: 1;
    color: var(--ink);
  }

  .person { position: absolute; right: 27px; top: 132px; text-align: right; }
  .person__name {
    font-family: "Titillium Web", sans-serif;
    font-weight: 700;
    font-size: 19px;
    color: var(--deep-green);
    line-height: 1.1;
  }
  .person__role { font-size: 16px; color: var(--slate); line-height: 1.2; }

  .rule {
    position: absolute;
    left: 340px;
    right: 0;
    top: 193px;
    height: 2px;
    background: linear-gradient(90deg, rgba(79,154,44,0), var(--mid-green) 40%);
  }

  .contact {
    position: absolute;
    right: 27px;
    top: 212px;
    list-style: none;
    text-align: right;
  }
  .contact li {
    font-size: 14.5px;
    color: var(--ink);
    line-height: 22px;
    display: flex;
    align-items: center;
    justify-content: flex-end;
    gap: 6px;
  }
  .contact svg { width: 11px; height: 11px; flex: none; }

  .photo {
    position: absolute;
    inset: 0;
    background:
      radial-gradient(circle at 40% 40%, #d9b59a 0 14%, transparent 30%),
      linear-gradient(135deg, #b8d8e6 0%, #8cc36a 35%, #e9d46a 55%, #e7864a 75%, #9fd0dc 100%);
  }

  .banner { position: absolute; inset: 0; }
  .slogan {
    position: absolute;
    left: 379px;
    top: 84px;
    font-family: "Signika", sans-serif;
    font-weight: 700;
    font-variant: small-caps;
    font-size: 40px;
    line-height: 48px;
    color: var(--paper);
  }
</style>
</head>
<body>

  <section class="card card--front">
    <div class="accent-band" role="img" aria-label="Curved grey and green ribbon decoration"></div>

    <div class="brand">
      <span class="brand__name">Zintaro</span>
      <span class="brand__dot"></span>
    </div>

    <div class="person">
      <p class="person__name">Martin Oakes</p>
      <p class="person__role">CEO</p>
    </div>
    <div class="rule"></div>

    <ul class="contact">
      <li>+44 7912 584 207
        <svg viewBox="0 0 12 12" aria-hidden="true"><circle cx="6" cy="6" r="6" fill="var(--mid-green)"/><path d="M4 3 L5 3 L5.6 4.6 L4.9 5.2 C5.3 6.1 5.9 6.7 6.8 7.1 L7.4 6.4 L9 7 L9 8 C6 8.5 3.5 6 4 3Z" fill="#fff"/></svg>
      </li>
      <li>martino@zintaropq.com
        <svg viewBox="0 0 12 12" aria-hidden="true"><circle cx="6" cy="6" r="6" fill="var(--mid-green)"/><rect x="3" y="4" width="6" height="4.2" fill="#fff"/><path d="M3 4 L6 6.4 L9 4" fill="none" stroke="var(--mid-green)" stroke-width=".8"/></svg>
      </li>
      <li>www.zintaropq.com
        <svg viewBox="0 0 12 12" aria-hidden="true"><circle cx="6" cy="6" r="6" fill="var(--mid-green)"/><circle cx="6" cy="6" r="3.2" fill="none" stroke="#fff" stroke-width=".8"/><path d="M2.8 6 H9.2 M6 2.8 V9.2" stroke="#fff" stroke-width=".7"/></svg>
      </li>
    </ul>
  </section>

  <section class="card card--back">
    <div class="photo" role="img" aria-label="Photo of a man in a green shirt covered in colourful sticky notes, looking up"></div>
    <svg class="banner" viewBox="0 0 525 300" aria-hidden="true">
      <defs>
        <linearGradient id="bannerFill" x1="0" y1="0" x2="1" y2="0">
          <stop offset="0" stop-color="var(--deep-green)"/>
          <stop offset="1" stop-color="#6db33f"/>
        </linearGradient>
      </defs>
      <polygon points="331,42 525,15 525,262 331,277" fill="url(#bannerFill)"/>
    </svg>
    <p class="slogan">Work<br>You<br>Way</p>
  </section>

</body>
</html>
```